Austrian finance und insurance broker needs business card design

We Need a serious looking Design for Business Card. we consult private and corporates customers in finance and insurance questions. the final design should express security and experience. We consult customers in questions of loans, Investments and insurance and have a wide range of Banks to offer. We compare several offers and select the best for our customers.

Target Market(s)

private and coporate customers with efforts in Money and insurance

Industry/Entity Type

Insurance Broker

Contact Information for Business Card

Martin Brauneder
Geschäftsführer
staatl. geprüfter Vermögensberater und Versicherungsmakler
Tel: 0664 512 8049
office@der-brauneder.at
www.der-brauneder.at
Anton Weibl Gasse 14
2135 Halbach
GISA Nr. 40527318 u. 40816493 (backside)

Font styles to use
Serif
Sans Serif

Requirements
Must have
• logo (designcrowd zip) and all Details
Nice to have
• makler logo design, maybe a 2 coloured Version is possible

```html
<!DOCTYPE html>
<html lang="de">
<head>
<meta charset="utf-8">
<title>Brauneder Finanz – Visitenkarte</title>
<link rel="stylesheet" href="https://fonts.googleapis.com/css2?family=Poppins:wght@400;500;600&display=swap">
<style>
  :root {
    --stage: #1d1e20;
    --brand-blue: #2b5caa;
    --paper: #ffffff;
    --swoosh-grey: #6b6b6b;
    --ink-grey: #4a4a4a;
    --seal-red: #b3262b;
    --on-blue: #ffffff;
  }
  * { box-sizing: border-box; margin: 0; padding: 0; }
  html, body { width: 1200px; height: 852px; overflow: hidden; }
  body {
    background: var(--stage);
    font-family: "Poppins", sans-serif;
    position: relative;
  }
  .card {
    position: absolute;
    left: 290px;
    width: 620px;
    height: 354px;
    border-radius: 18px;
    overflow: hidden;
    background: var(--brand-blue);
    color: var(--on-blue);
  }
  .card--back { top: 46px; }
  .card--front { top: 452px; }

  /* Back */
  .brand {
    position: absolute;
    display: flex;
    align-items: center;
    gap: 12px;
    font-weight: 600;
  }
  .brand__dot {
    width: 22px; height: 22px; border-radius: 50%;
    background: currentColor;
  }
  .card--back .brand { left: 150px; top: 140px; font-size: 30px; }
  .card--back .brand__dot { width: 30px; height: 30px; }
  .gisa {
    position: absolute;
    right: 48px; bottom: 48px;
    font-size: 15px;
    letter-spacing: 0.5px;
  }

  /* Front */
  .front-art { position: absolute; inset: 0; }
  .card--front .brand {
    color: var(--brand-blue);
    right: 40px; top: 36px;
    font-size: 20px;
  }
  .badge {
    position: absolute;
    right: 52px; top: 92px;
    width: 34px; height: 34px; border-radius: 50%;
    background: var(--seal-red);
  }
  .address {
    position: absolute;
    right: 40px; top: 150px;
    text-align: right;
    color: var(--ink-grey);
    font-size: 17px;
    line-height: 1.35;
  }
  .person {
    position: absolute;
    left: 44px; bottom: 24px;
  }
  .person__name { font-size: 30px; font-weight: 500; line-height: 1.1; }
  .person__role { font-size: 14px; line-height: 1.35; margin-top: 4px; }
  .contact { list-style: none; margin-top: 12px; font-size: 16px; line-height: 1.45; }
  .contact li { display: flex; align-items: center; gap: 10px; }
  .contact svg { width: 13px; height: 13px; fill: none; stroke: var(--on-blue); stroke-width: 1.8; }
</style>
</head>
<body>

<section class="card card--back">
  <div class="brand"><span class="brand__dot"></span>Brauneder Finanz GmbH</div>
  <p class="gisa">GISA Nr. 40527318 u. 40816493</p>
</section>

<section class="card card--front">
  <svg class="front-art" viewBox="0 0 620 354" preserveAspectRatio="none" aria-hidden="true">
    <path d="M250 0 C 280 170 430 262 620 250 L620 0 Z" fill="var(--paper)"/>
    <path d="M250 0 C 280 170 430 262 620 250" fill="none" stroke="var(--swoosh-grey)" stroke-width="7"/>
    <path d="M240 0 C 270 184 430 276 620 264" fill="none" stroke="var(--paper)" stroke-width="2"/>
  </svg>

  <div class="brand"><span class="brand__dot"></span>Brauneder Finanz GmbH</div>
  <div class="badge" role="img" aria-label="Maklerabzeichen"></div>
  <p class="address">Anton Weibl Gasse 14<br>2135 Halbach</p>

  <div class="person">
    <h1 class="person__name">Martin Brauneder</h1>
    <p class="person__role">Geschäftsführer<br>staatl. geprüfter Vermögensberater<br>und Versicherungsmakler</p>
    <ul class="contact">
      <li><svg viewBox="0 0 16 16"><path d="M4 1.5l2.5 3-1.5 1.8c.8 1.8 2.2 3.2 4 4l1.8-1.5 3 2.5-1.5 2.5C7 13.5 2.5 9 1.5 3z"/></svg>0664 512 8049</li>
      <li><svg viewBox="0 0 16 16"><rect x="1.5" y="3.5" width="13" height="9"/><path d="M1.5 3.5L8 9l6.5-5.5"/></svg>office@der-brauneder.at</li>
      <li><svg viewBox="0 0 16 16"><circle cx="8" cy="8" r="6.5"/><path d="M1.5 8h13M8 1.5c-3 3.5-3 9.5 0 13M8 1.5c3 3.5 3 9.5 0 13"/></svg>www.der-brauneder.at</li>
    </ul>
  </div>
</section>

</body>
</html>
```